Flyer-Design für traditionelles Dorffest
Zielgruppe
Benötigen Flyer/Plakat design A4 Doppelseite für traditionelles Dorffest.
Aufgabenstellung
Das Design soll einem traditionellen Dorffest der Schützenkompanie entsprechen. (Farben: Dunkelgrün oder Rot / Weiß)
Text Vorderseite:
- Die Schützenkompanie Obermoosbach lädt zum Obermoosbacher Dorffest. (Überschrift Obermoosbacher Dorffest groß)
- Samstag 10. August 2019
- Erstmals mit 'Riesen-Fußball-Dart' Turnier ab 14 Uhr
- 17 Uhr Einmarsch der Musikkapelle Obermoosbach mit anschließendem Konzert im Festzelt
- Stimmungsabend mit 'Die fesch'n Gamsler'
- zugestellt durch briefweg.at an einen Haushalt (Kleiner Hinweiß rechts oben)
- Eintritt: 5€ (Kleiner Schriftzug)
- Mit Schießbude, Wein- und Kaffeebar, Weißbierbar, Schützenbar und großer Tombola
Logos Vorderseite:
- Logo Musik 'Die fesch'n Gamsler'.
- Tiroler Adler (Schützen) Eventuell im Hintergrund oder Modifizieren
- Eventuell Bild von Hinterthiersee mit einbauchen (Hintergrund)
Text Hinterseite:
- Überschrift groß: 'Riesen-Fußball-Dart' Turnier
- Beginn um 14 Uhr
- 3 Spieler pro Team
- Startgebühr: 30 € pro Team (Damen, Herren oder Mixed Teams möglich) / Kinderteams 15 €
- Für Unfälle jeglicher Art wird vom Veranstalter keine Haftung übernommen! (Kleine Schrift)
- Wir achten auf den Jugendschutz! (Kleine Schrift)
- Überschrift groß: 'Heimfahrservice innerhalb von Thiersee'
Auf Euer Kommen freut sich die Schützenkompanie Obermoosbach!
Logos Rückseite Sponsoren: Kornkasse Bergtal, Laufwerker Obermoosbach, Jausenstation Brunnalm, Loidlmayr Bau, Metzgerei Stangl, Zitherbau Egger, varolin GmbH, Sanitär Technik Aubing
Logos im Anhang. Foto von Hinterthiersee und Tiroler Adler bei Bedarf via Mail (Da nicht mehr Anhänge möglich sind).
Bei Fragen freue Ich mich über Ihre Nachricht.
Vielen Dank für die Vorschläge.

```html
<!DOCTYPE html>
<html lang="de">
<head>
<meta charset="utf-8">
<title>Obermoosbacher Dorffest</title>
<link rel="stylesheet" href="https://fonts.googleapis.com/css2?family=Dela+Gothic+One&family=Barlow+Condensed:wght@600&display=swap">
<style>
  :root {
    --meadow-light: #6f9a55;
    --meadow-dark: #3c5d33;
    --crowd-dark: #3a3a30;
    --panel-green: rgba(38, 86, 56, 0.84);
    --ink-white: #ffffff;
  }
  html, body {
    margin: 0;
    padding: 0;
    overflow: hidden;
  }
  .flyer {
    position: relative;
    width: 848px;
    height: 1200px;
    overflow: hidden;
    background: #ffffff;
  }
  .backdrop-photo {
    position: absolute;
    inset: 0;
    background:
      linear-gradient(180deg, #4d6a52 0%, #556353 25%, var(--crowd-dark) 45%, #4f5a3a 62%, var(--meadow-dark) 75%, var(--meadow-light) 100%);
  }
  .panel {
    position: absolute;
    left: 37px;
    top: 49px;
    width: 775px;
    height: 1103px;
    background: var(--panel-green);
  }
  .frame {
    position: absolute;
    left: 0;
    top: 0;
  }
  .copy {
    position: absolute;
    left: 0;
    top: 0;
    width: 848px;
    height: 1200px;
    color: var(--ink-white);
  }
  .display {
    font-family: "Dela Gothic One", "Arial Black", sans-serif;
    position: absolute;
    left: 87px;
    margin: 0;
    font-weight: 400;
    white-space: nowrap;
  }
  .intro {
    top: 132px;
    font-size: 34px;
    line-height: 49px;
    letter-spacing: 0.5px;
  }
  .headline {
    top: 270px;
    font-size: 58px;
    line-height: 72px;
  }
  .date {
    top: 488px;
    font-size: 35px;
    line-height: 44px;
  }
  .programme {
    position: absolute;
    left: 86px;
    top: 585px;
    width: 670px;
    margin: 0;
    padding: 0;
    list-style: none;
    font-family: "Barlow Condensed", "Arial Narrow", sans-serif;
    font-weight: 600;
    font-size: 21px;
    line-height: 27px;
  }
  .programme li {
    position: relative;
    padding-left: 14px;
    margin-bottom: 28px;
  }
  .programme li::before {
    content: "";
    position: absolute;
    left: 1px;
    top: 11px;
    width: 6px;
    height: 6px;
    border-radius: 50%;
    background: var(--ink-white);
  }
  .band-badge {
    position: absolute;
    left: 486px;
    top: 735px;
    width: 240px;
    height: 100px;
    background: var(--ink-white);
    transform: rotate(6deg);
    display: flex;
    align-items: center;
    justify-content: center;
  }
  .band-badge span {
    font-family: "Barlow Condensed", "Arial Narrow", sans-serif;
    font-weight: 600;
    font-size: 24px;
    color: #2a2a22;
  }
  .amenities {
    top: 866px;
    font-size: 27px;
    line-height: 31px;
    white-space: normal;
    width: 690px;
  }
  .admission {
    top: 1022px;
    font-size: 19px;
    line-height: 24px;
  }
  .horn-illustration {
    position: absolute;
    left: 366px;
    top: 958px;
    width: 318px;
    height: 146px;
    border-radius: 70px;
    background: rgba(255, 255, 255, 0.14);
  }
</style>
</head>
<body>
<main class="flyer">
  <div class="backdrop-photo" role="img" aria-label="Foto: Schützen in Tracht vor Festpublikum auf einer Dorfwiese"></div>
  <div class="panel"></div>

  <svg class="frame" width="848" height="1200" viewBox="0 0 848 1200" aria-hidden="true">
    <g fill="none" stroke="#ffffff">
      <rect x="48" y="68" width="752" height="1069" stroke-width="2"/>
      <rect x="53" y="73" width="742" height="1059" stroke-width="1"/>
    </g>
  </svg>

  <section class="copy">
    <p class="display intro">Die Schützenkompanie<br>Obermoosbach lädt um</p>
    <h1 class="display headline">Obermoosbacher<br>Dorffest.</h1>
    <p class="display date">Samstag 10. August 2019</p>

    <ul class="programme">
      <li>Erstmals mit ‚Riesen-Fußball-Dart‘ Turnier ab 14 Uhr</li>
      <li>17 Uhr Einmarsch der Musikkapelle Obermoosbach mit anschließendem Konzert im Festzelt</li>
      <li>Stimmungsabend mit ‚Die fesch‘n Gamsler‘</li>
    </ul>

    <div class="band-badge"><span>Die fesch'n Gamsler</span></div>

    <p class="display amenities">Mit Schießbude, Wein- und Kaffeebar, Weißbierbar, Schützenbar und großer Tombola</p>
    <p class="display admission">Eintritt: 5€</p>

    <div class="horn-illustration" role="img" aria-label="Illustration: weißes Posthorn mit Klangstrichen"></div>
  </section>
</main>
</body>
</html>
```